Real estate company needs a letterhead design

A young real estate company needs a letterhead / stationery design, it should include the company's logo. It should look exactly the same as on the business cards. (With the phrase "a brand of FEO Immobilien & Projektentwicklung GmbH")

In addition, it should also include the 4 round seals.

color code blue # 00456b gray # 333333

Word and PDF are welcome.

FEO Immobilien & Projektentwicklung GmbH
Managing director: Mag. Lukas Strenhofer
Anton-Wiesmayr-Strasse 3c / 41
6300 Wörgl

Tel .: +436645917283
Email: office@wohnquell.example
Web: www.wohnquell.example

Sparkasse Almhofen, Bergländer Sparkasse from 1893, Gildenkasse
Ferdinand-Moosrainer-Strasse 9, 6300 Wörgl
IBAN: AT31 4819 2093 5521 6604
BIC: GLMRAT31XXX
Account holder: FEO Immobilien & Projektentwicklung GmbH

FN: XXXXXXX
UID: XXXXXXX

```html
<!DOCTYPE html>
<html lang="en">
<head>
<meta charset="utf-8">
<title>WOHNQUELL Stationery</title>
<link href="https://fonts.googleapis.com/css2?family=Montserrat:wght@700&family=Roboto+Condensed:wght@400;700&family=Roboto:wght@400&display=swap" rel="stylesheet">
<style>
  :root {
    --brand-blue: #00456b;
    --text-gray: #333333;
    --muted-gray: #555555;
    --backdrop: #a9a7a8;
    --paper: #ffffff;
    --seal-red: #d0282b;
  }
  * { margin: 0; padding: 0; box-sizing: border-box; }
  html, body { width: 1200px; height: 770px; overflow: hidden; background: var(--backdrop); }
  .stage { position: relative; width: 1200px; height: 770px; }

  .wordmark {
    position: absolute;
    font-family: "Montserrat", sans-serif;
    font-weight: 700;
    color: var(--brand-blue);
    letter-spacing: 0.5px;
    white-space: nowrap;
  }

  /* Letterhead */
  .letterhead { position: absolute; left: 94px; top: 63px; width: 456px; height: 643px; background: var(--paper); }
  .letterhead__frame { position: absolute; left: 9px; top: 10px; width: 437px; height: 623px; border: 2px solid var(--brand-blue); }
  .letterhead .wordmark { left: 46px; top: 62px; font-size: 22px; }

  .sender {
    position: absolute; right: 49px; top: 48px; text-align: right;
    font-family: "Roboto Condensed", sans-serif; font-size: 6.2px; line-height: 8.4px; color: var(--text-gray);
  }
  .sender__company { color: var(--brand-blue); font-weight: 700; }
  .sender__contacts { margin-top: 5px; }
  .sender__line { display: flex; justify-content: flex-end; align-items: center; gap: 3px; }
  .sender__line svg { width: 6px; height: 6px; fill: var(--brand-blue); }

  .recipient {
    position: absolute; left: 46px; top: 160px;
    font-family: "Roboto", sans-serif; font-size: 7.6px; line-height: 10.8px; color: var(--muted-gray);
  }
  .letter-date {
    position: absolute; right: 49px; top: 160px;
    font-family: "Roboto", sans-serif; font-size: 7.4px; color: var(--muted-gray);
  }
  .salutation {
    position: absolute; left: 47px; top: 246px;
    font-family: "Roboto", sans-serif; font-size: 9.6px; color: var(--text-gray);
  }
  .letter-body {
    position: absolute; left: 47px; top: 268px; width: 360px;
    font-family: "Roboto", sans-serif; font-size: 7.1px; line-height: 10.8px; color: var(--muted-gray);
    text-align: justify;
  }
  .letter-body p + p { margin-top: 10.8px; }
  .closing {
    position: absolute; left: 47px; top: 463px;
    font-family: "Roboto", sans-serif; font-size: 7.2px; color: var(--muted-gray);
  }
  .signature-area { position: absolute; left: 47px; top: 488px; width: 58px; height: 26px; background: linear-gradient(90deg, #eef1f4, #dfe6ec); border-radius: 3px; }

  .footer-rule { position: absolute; top: 559px; height: 1px; background: var(--brand-blue); }
  .footer-rule--left { left: 46px; width: 118px; }
  .footer-rule--right { left: 289px; width: 118px; }
  .seal { position: absolute; top: 546px; width: 26px; height: 26px; border-radius: 50%; background: var(--paper); border: 1px solid var(--seal-red); }
  .seal::after { content: ""; position: absolute; left: 4px; top: 4px; width: 16px; height: 16px; border-radius: 50%; background: var(--seal-red); }

  .bank, .legal {
    position: absolute; top: 573px;
    font-family: "Roboto Condensed", sans-serif; font-size: 6px; line-height: 8.7px; color: var(--text-gray);
  }
  .bank { left: 46px; }
  .legal { right: 49px; text-align: right; }
  .legal b { color: var(--brand-blue); font-weight: 700; }

  /* Envelope back with flap */
  .envelope-back { position: absolute; left: 644px; top: 331px; width: 508px; height: 251px; background: var(--paper); }
  .envelope-back__flap { position: absolute; left: 0; top: 0; width: 508px; height: 82px; }
  .envelope-back .wordmark { left: 0; width: 508px; text-align: center; top: 39px; font-size: 15px; color: var(--paper); }

  /* Envelope front */
  .envelope-front { position: absolute; left: 584px; top: 455px; width: 508px; height: 251px; background: var(--paper); }
  .envelope-front__frame { position: absolute; left: 10px; top: 10px; width: 488px; height: 231px; border: 2px solid var(--brand-blue); }
  .envelope-front .wordmark { left: 38px; top: 42px; font-size: 19px; }
  .envelope-front__sender {
    position: absolute; left: 38px; top: 68px;
    font-family: "Roboto Condensed", sans-serif; font-size: 6.2px; line-height: 8.4px; color: var(--text-gray);
  }
  .envelope-front__sender .sender__company { color: var(--brand-blue); font-weight: 700; }
</style>
</head>
<body>
<main class="stage">

  <section class="letterhead">
    <div class="letterhead__frame"></div>
    <div class="wordmark">WOHNQUELL</div>

    <address class="sender" style="font-style:normal">
      <div class="sender__company">FEO Immobilien &amp; Projektentwicklung GmbH</div>
      <div>Managing director: Mag. Lukas Strenhofer</div>
      <div>Anton-Wiesmayr-Strasse 3c / 41, 6300 Wörgl</div>
      <div class="sender__contacts">
        <div class="sender__line">+436645917283
          <svg viewBox="0 0 10 10"><path d="M2 0.5l2 2-1 1.3c.6 1.3 1.5 2.2 2.8 2.8l1.3-1 2 2-1.2 1.9C4.5 9.2.8 5.5.5 1.6z"/></svg></div>
        <div class="sender__line">office@wohnquell.example
          <svg viewBox="0 0 10 10"><path d="M0 2h10v6H0z M0 2l5 3.5L10 2" stroke="#fff" stroke-width="0.8"/></svg></div>
        <div class="sender__line">www.wohnquell.example
          <svg viewBox="0 0 10 10"><circle cx="5" cy="5" r="4.2" fill="none" stroke="#00456b" stroke-width="0.9"/><path d="M1 5h8M5 1v8" stroke="#00456b" stroke-width="0.7"/></svg></div>
      </div>
    </address>

    <div class="recipient">
      Companyname GmbH<br>Firstname Lastname<br>Adresse 10<br>40303 Cityname<br>Germany
    </div>
    <div class="letter-date">Germany - 08/06/2020</div>

    <div class="salutation">Dear Mr. Smith,</div>
    <div class="letter-body">
      <p>Lorem ipsum dolor sit amet, consectetur adipiscing elit. Donec orci purus, luctus vitae dignissim eu, iaculis sed purus. Vivamus faucibus, ipsum nec aliquet viverra, leo mauris condimentum ligula, sit amet sagittis enim ligula quis arcu. Nam egestas tortor id nisi porttitor mattis. In tortor ante, ultricies in suscipit a, tempus non massa. Vivamus et auctor mi. Fusce vel massa nulla. Phasellus nec eros mauris, et scelerisque orci.</p>
      <p>Donec malesuada orci vitae nulla accumsan porta a id massa. Quisque accumsan iaculis magna sit amet fringilla. Maecenas consequat, magna eget tincidunt semper, odio nibh rutrum mi, id feugiat ante nisi eu risus. Vestibulum nunc orci, rhoncus a placerat in, ultricies in mi. Cras mattis varius eros, vel fringilla nisi suscipit eget. Quisque scelerisque sagittis nulla at porttitor.</p>
      <p>Sed id augue vitae urna euismod commodo aliquet a quam. Pellentesque arcu velit, cursus et malesuada ut, consequat et diam. Nullam erat sem, rhoncus id ullamcorper vitae, rhoncus et arcu. In ultricies ultricies nulla, ut rutrum nisi iaculis at. Donec eu magna a metus ornare faucibus. Fusce aliquet faucibus ultricies. Morbi semper, est id tincidunt gravida, sem arcu adipiscing lacus, ac bibendum nulla leo eu purus. Quisque nec diam sed risus consectetur a ccumsan quis quis nibh. Vestibulum id purus lorem.</p>
    </div>

    <div class="closing">Sincerely,</div>
    <div class="signature-area" role="img" aria-label="Handwritten signature of the managing director"></div>

    <div class="footer-rule footer-rule--left"></div>
    <div class="footer-rule footer-rule--right"></div>
    <div class="seal" style="left:169px"></div>
    <div class="seal" style="left:199px"></div>
    <div class="seal" style="left:229px"></div>
    <div class="seal" style="left:259px"></div>

    <div class="bank">
      Sparkasse Almhofen<br>Bergländer Sparkasse from 1893<br>Gildenkasse<br>Ferdinand-Moosrainer-Strasse 9<br>6300 Wörgl
    </div>
    <div class="legal">
      <b>IBAN:</b> AT31 4819 2093 5521 6604<br>
      <b>BIC:</b> GLMRAT31XXX<br>
      <b>Account holder:</b> FEO Immobilien &amp;<br>
      Projektentwicklung GmbH<br>
      <b>FN:</b> 5120384&nbsp; <b>UID:</b> 7342019
    </div>
  </section>

  <section class="envelope-back">
    <svg class="envelope-back__flap" viewBox="0 0 508 82" aria-hidden="true">
      <path d="M0 0H508L494 52Q488 81 460 81H48Q20 81 14 52Z" fill="#00456b"/>
    </svg>
    <div class="wordmark">WOHNQUELL</div>
  </section>

  <section class="envelope-front">
    <div class="envelope-front__frame"></div>
    <div class="wordmark">WOHNQUELL</div>
    <div class="envelope-front__sender">
      <div class="sender__company">FEO Immobilien &amp; Projektentwicklung GmbH</div>
      <div>Managing director: Mag. Lukas Strenhofer</div>
      <div>Anton-Wiesmayr-Strasse 3c / 41, 6300 Wörgl</div>
    </div>
  </section>

</main>
</body>
</html>
```